Health care center needs brochure design

We need a set of brochure designs for the 4 sections of our clinic, color coded based on the brand guidelines and with introduced icons to every section. The three sections include Biological Medicine (main medication tool is the IV tool), The Brindle Path program (main medication tool are the detox tools) , the Aesthetics section ( main medication tool is the syringe) and the lab (main tool is the microscope). You can find out more about our sections in the website www.velnortaclinic-example.com. The use of elements of the brand itself such as the lotus is also applicable.

Industry/Entity Type

Health Care

Requirements
Must have
• use of brand identity colors and features
• reflective medical icons
• color coding for each of the 4 sections based on the brand colors
Should not have
• pictures overused by other health care providers

```html
<!DOCTYPE html>
<html lang="en">
<head>
<meta charset="utf-8">
<title>Swiss Biological Medicine – Brochure</title>
<link rel="stylesheet" href="https://fonts.googleapis.com/css2?family=Oswald:wght@300;500;600&family=Lato:ital,wght@0,300;0,400;0,700;1,400;1,700&display=swap">
<style>
  :root{
    --green:#7fcaa6;
    --green-dark:#5bb48a;
    --orange:#f4a67f;
    --ink:#4b4b4b;
    --panel:#f1f1ef;
    --paper:#ffffff;
    --stage:#b9bec6;
  }
  *{box-sizing:border-box;margin:0;padding:0}
  html,body{width:1200px;height:1200px;overflow:hidden}
  body{background:var(--stage);font-family:'Lato',sans-serif;color:var(--ink)}
  .brochure{position:absolute;left:200px;top:35px;width:800px;height:1130px;background:var(--paper);overflow:hidden;box-shadow:0 6px 24px rgba(0,0,0,.18)}
  .brochure-shapes{position:absolute;inset:0}

  .title{position:absolute;left:36px;top:150px;font-family:'Oswald',sans-serif;line-height:.95;font-weight:normal}
  .title span{display:block}
  .title-swiss{display:flex !important;align-items:center;gap:12px;font-weight:600;font-size:46px;color:var(--ink);letter-spacing:-1px}
  .title-swiss::after{content:"";width:90px;height:2px;background:var(--orange);margin-top:16px}
  .title-biological{font-weight:600;font-size:66px;color:var(--green);letter-spacing:-2px}
  .title-medicine{font-weight:300;font-size:70px;color:var(--orange);letter-spacing:-1px}

  .clinic-name{position:absolute;left:130px;top:662px;display:flex;align-items:center;gap:12px}
  .clinic-dot{width:56px;height:56px;border-radius:50%;background:var(--green)}
  .clinic-text{color:var(--green-dark);font-weight:400;font-size:17px;line-height:1.05;text-transform:uppercase}
  .clinic-text small{display:block;font-size:10px;letter-spacing:1px;margin-bottom:3px}

  .about{position:absolute;left:40px;top:742px;width:420px}
  .section-heading{color:var(--green-dark);font-weight:400;font-size:22px;line-height:1.05;text-transform:uppercase}
  .section-heading strong{font-weight:700;display:block}
  .about p{font-size:12px;line-height:1.4;margin-top:8px}
  .factors{display:flex;margin-top:12px}
  .factors ul{list-style:none;font-size:13px;line-height:1.55}
  .factors-left{width:180px;font-weight:700;font-style:italic}
  .factors-divider{width:2px;background:var(--orange);margin-right:18px;height:118px}
  .factors-right{width:220px}
  .factors-right li{position:relative;padding-left:16px;font-size:12.5px;white-space:nowrap}
  .factors-right li::before,.conditions li::before{content:"";position:absolute;left:0;top:.55em;width:7px;height:7px;border-radius:50%;background:var(--green)}
  .about .closing{margin-top:8px}

  .treat{position:absolute;left:480px;top:625px;width:290px}
  .conditions{list-style:none;margin-top:10px}
  .conditions li{position:relative;padding-left:18px;font-size:12.5px;line-height:1.75}
  .treat-rule{width:110px;height:2px;background:var(--orange);margin:12px 0 10px}
  .restore{font-size:17px;font-weight:300;line-height:1.25}
  .steps{list-style:none;margin-top:8px;counter-reset:step}
  .steps li{position:relative;padding-left:20px;font-size:11px;line-height:1.35;margin-bottom:3px;counter-increment:step}
  .steps li::before{content:counter(step);position:absolute;left:0;top:1px;width:13px;height:13px;border-radius:50%;background:var(--green);color:#fff;font-size:9px;text-align:center;line-height:13px;font-weight:700}

  .contact{position:absolute;left:40px;top:1053px;color:var(--paper);font-size:11.5px;line-height:1.3;font-style:normal}
  .contact strong{font-weight:700}
</style>
</head>
<body>
<main class="brochure">
  <svg class="brochure-shapes" viewBox="0 0 800 1130" width="800" height="1130" xmlns="http://www.w3.org/2000/svg">
    <defs>
      <linearGradient id="pharmacyTones" x1="0" y1="0" x2="1" y2="1">
        <stop offset="0" stop-color="#e9ecef"/>
        <stop offset=".45" stop-color="#f3eeea"/>
        <stop offset="1" stop-color="#c9d3d8"/>
      </linearGradient>
      <linearGradient id="valleyTones" x1="0" y1="0" x2="0" y2="1">
        <stop offset="0" stop-color="#dfe5ea"/>
        <stop offset=".45" stop-color="#9aa59a"/>
        <stop offset="1" stop-color="#5f7d45"/>
      </linearGradient>
    </defs>
    <path d="M0 700 C170 610 340 545 520 525 C620 515 720 515 800 510 L800 1130 L0 1130 Z" fill="var(--panel)"/>
    <path d="M190 0 C260 20 310 50 340 90 L360 60 C330 30 300 10 270 0 Z" fill="var(--orange)"/>
    <path d="M270 0 C320 20 355 45 375 75 L400 40 L400 0 Z" fill="var(--green)"/>
    <circle cx="620" cy="230" r="290" fill="var(--green)"/>
    <g role="img" aria-label="Photo of a pharmacist showing a medicine bottle to an older customer in a pharmacy">
      <circle cx="632" cy="218" r="262" fill="url(#pharmacyTones)"/>
    </g>
    <path d="M0 590 C130 520 280 470 440 450 C300 490 150 550 0 635 Z" fill="var(--orange)"/>
    <path d="M0 640 C160 560 330 500 500 485 C620 475 720 480 800 470 L800 510 C720 515 620 515 520 525 C340 545 170 610 0 700 Z" fill="var(--green)"/>
    <path d="M750 545 L800 520 L800 600 Z" fill="var(--green)"/>
    <path d="M730 590 L800 570 L800 680 C785 640 765 605 730 590 Z" fill="var(--orange)"/>
    <path d="M470 1058 L800 1022 L800 1029 L470 1065 Z" fill="var(--green)"/>
    <g role="img" aria-label="Photo of a green alpine valley village beneath mountains">
      <path d="M470 1065 L800 1029 L800 1130 L470 1130 Z" fill="url(#valleyTones)"/>
    </g>
    <path d="M0 1046 L430 1046 C455 1046 470 1060 470 1085 L470 1130 L0 1130 Z" fill="var(--green)"/>
  </svg>

  <h1 class="title">
    <span class="title-swiss">SWISS</span>
    <span class="title-biological">BIOLOGICAL</span>
    <span class="title-medicine">MEDICINE</span>
  </h1>

  <div class="clinic-name">
    <span class="clinic-dot"></span>
    <p class="clinic-text"><small>Dr. Lina Haddad</small>Integrated<br>Care Center</p>
  </div>

  <section class="about">
    <h2 class="section-heading">What is <strong>Biological Medicine?</strong></h2>
    <p>Biological medicine looks for the underlying source of illness. These root causes may consist of several factors that, over time, can allow disease causing toxins to build up in the body. Some of these underlying factors include:</p>
    <div class="factors">
      <ul class="factors-left">
        <li>Diet</li>
        <li>Food allergies</li>
        <li>Intestinal disturbances</li>
        <li>Family history</li>
        <li>Emotional stress</li>
        <li>Environmental</li>
      </ul>
      <span class="factors-divider"></span>
      <ul class="factors-right">
        <li>Heavy metals</li>
        <li>Dental disturbances</li>
        <li>Hyperacidity</li>
        <li>Trauma</li>
        <li>Exposure to bacteria or viruses</li>
        <li>Electromagnetic disturbances</li>
      </ul>
    </div>
    <p class="closing">Without fundamental changes in these root causes, there can be no real healing.</p>
  </section>

  <section class="treat">
    <h2 class="section-heading">Conditions <strong>We Treat</strong></h2>
    <ul class="conditions">
      <li>Autoimmune Diseases</li>
      <li>Cancer</li>
      <li>Cardiovascular Diseases and Hypertension</li>
      <li>Intestinal and Digestive Disorders</li>
      <li>Joint Pain and Bone Health</li>
      <li>Lyme and Chronic Infections</li>
      <li>Metabolic and Degenerative Conditions</li>
      <li>Neurological Disorders</li>
    </ul>
    <div class="treat-rule"></div>
    <p class="restore">Restoring the body with biological medicine is done through:</p>
    <ol class="steps">
      <li>Detoxification,</li>
      <li>Rebuilding the digestive system,</li>
      <li>Strengthening the immune system and alkalizing your body through diet, to support the proper pH, one of the most important foundations of health.</li>
    </ol>
  </section>

  <address class="contact">
    <strong>Dr. Lina Haddad Integrated Care Center</strong><br>
    P.O. Box 40210, Cedar Walk, Harbor District<br>
    United Arab Emirates<br>
    +971 4 555 0142<br>
    www.velnortaclinic-example.com
  </address>
</main>
</body>
</html>
```